Business Card Design

We offer full auto repair and auto customization from custom wheels to lift kits and drop kits we do it all. I want something that grabs your attention from the start but nothing flashy i am more of a clean crisp modern kinda of guy. I plan on using the design on my business cards and my main business sign .
Updates
I have up loaded an image of my currant business card designed by me , I would like to improve on it
Target Market(s)
20-35 male and female
Industry/Entity Type
Business
Contact Information for Business Card
Calloway Tire Service
48306 1/2 Pruett rd
Houston TX, 77391
Manager: Gavin Alcott
P:832-555-0147
F:832-555-0182
Email:Gavin@callowayautoandtire.example
website:Callowayautoandtire.example
Look and feel

```html
<!DOCTYPE html>
<html lang="en">
<head>
<meta charset="utf-8">
<title>Calloway Tire Service – Business Card</title>
<link rel="stylesheet" href="https://fonts.googleapis.com/css2?family=Open+Sans:wght@400;600;700&display=swap">
<style>
  :root {
    --page-bg: #e4e4e2;
    --charcoal: #4a4a4a;
    --panel-grey: #cdcecf;
    --panel-soft: #d8d9da;
    --panel-light: #f2f2f2;
    --brand-blue: #1450a8;
    --icon-blue: #3f86cf;
    --text-dark: #3a3a3a;
    --rule-grey: #c9c9c9;
  }
  * { box-sizing: border-box; margin: 0; padding: 0; }
  html, body { width: 1200px; height: 1173px; overflow: hidden; }
  body {
    background: var(--page-bg);
    font-family: "Open Sans", Arial, sans-serif;
    color: var(--text-dark);
    position: relative;
  }

  .card {
    position: absolute;
    top: 166px;
    width: 480px;
    height: 840px;
    padding: 28px;
    box-shadow: 0 10px 26px rgba(0,0,0,.18);
  }

  /* Front card */
  .card--front { left: 80px; background: var(--charcoal); }
  .front__header {
    height: 130px;
    background: var(--panel-grey);
    border-top-right-radius: 60px;
    display: flex; align-items: center; justify-content: center;
    font-size: 20px; letter-spacing: 1px; color: var(--text-dark);
    white-space: nowrap;
  }
  .front__divider { height: 12px; background: var(--charcoal); }
  .front__body {
    height: 642px;
    background: var(--panel-light);
    border-bottom-left-radius: 70px;
    display: flex; align-items: center; justify-content: center;
  }
  .brand { display: flex; align-items: center; gap: 18px; }
  .brand__mark { width: 26px; height: 26px; background: var(--brand-blue); }
  .brand__name {
    font-weight: 700; font-size: 34px; line-height: 1.15;
    color: var(--brand-blue);
  }

  /* Back card */
  .card--back { left: 640px; background: var(--brand-blue); }
  .back__inner {
    height: 100%;
    border-top-left-radius: 60px;
    border-bottom-right-radius: 70px;
    overflow: hidden;
    display: flex; flex-direction: column;
    background: var(--panel-light);
  }
  .back__header { height: 130px; background: var(--panel-grey); }
  .contact-list {
    list-style: none;
    flex: 1;
    padding: 36px 16px 0 24px;
  }
  .contact {
    display: flex; align-items: center; gap: 18px;
    height: 106px;
    position: relative;
  }
  .contact::after {
    content: ""; position: absolute; left: 70px; right: 0; bottom: 12px;
    height: 3px; background: var(--rule-grey);
  }
  .contact:last-child::after { display: none; }
  .contact__icon { width: 52px; height: 52px; flex: none; }
  .contact__text { font-size: 16px; line-height: 1.45; white-space: nowrap; }
  .back__footer {
    height: 210px;
    background: var(--panel-soft);
  }
  .person {
    height: 130px;
    background: var(--panel-grey);
    padding: 20px 0 0 100px;
  }
  .person__name { font-size: 31px; font-weight: 700; letter-spacing: 1px; line-height: 1.3; }
  .person__role { font-size: 26px; line-height: 1.3; }
</style>
</head>
<body>

<section class="card card--front">
  <header class="front__header">www.Callowayautoandtire.example</header>
  <div class="front__divider"></div>
  <div class="front__body">
    <div class="brand">
      <span class="brand__mark"></span>
      <span class="brand__name">Calloway<br>Tire Service</span>
    </div>
  </div>
</section>

<section class="card card--back">
  <div class="back__inner">
    <div class="back__header"></div>
    <ul class="contact-list">
      <li class="contact">
        <svg class="contact__icon" viewBox="0 0 60 60" aria-hidden="true">
          <circle cx="30" cy="30" r="27" fill="none" stroke="var(--icon-blue)" stroke-width="3"/>
          <path d="M22 16c3 0 4 6 2 8l-2 2c2 5 5 8 10 10l2-2c2-2 8-1 8 2v3c0 2-2 4-5 4C25 43 17 35 17 21c0-3 2-5 5-5z" fill="var(--icon-blue)"/>
        </svg>
        <span class="contact__text">P: 832-555-0147<br>F: 832-555-0182</span>
      </li>
      <li class="contact">
        <svg class="contact__icon" viewBox="0 0 60 60" aria-hidden="true">
          <circle cx="30" cy="30" r="27" fill="none" stroke="var(--icon-blue)" stroke-width="3"/>
          <rect x="16" y="20" width="28" height="20" fill="var(--icon-blue)"/>
          <path d="M16 20l14 11 14-11" fill="none" stroke="#fff" stroke-width="2"/>
        </svg>
        <span class="contact__text">Gavin@callowayautoandtire.example</span>
      </li>
      <li class="contact">
        <svg class="contact__icon" viewBox="0 0 60 60" aria-hidden="true">
          <circle cx="30" cy="30" r="27" fill="none" stroke="var(--icon-blue)" stroke-width="3"/>
          <g fill="none" stroke="var(--icon-blue)" stroke-width="2.5">
            <circle cx="30" cy="30" r="15"/>
            <ellipse cx="30" cy="30" rx="7" ry="15"/>
            <path d="M15 30h30M17 23h26M17 37h26"/>
          </g>
        </svg>
        <span class="contact__text">www.Callowayautoandtire.example</span>
      </li>
      <li class="contact">
        <svg class="contact__icon" viewBox="0 0 60 60" aria-hidden="true">
          <circle cx="30" cy="30" r="27" fill="none" stroke="var(--icon-blue)" stroke-width="3"/>
          <path d="M30 46C22 36 19 31 19 25a11 11 0 0 1 22 0c0 6-3 11-11 21z" fill="var(--icon-blue)"/>
          <circle cx="30" cy="25" r="4.5" fill="#fff"/>
        </svg>
        <span class="contact__text">48306 1/2 Pruett rd<br>Houston TX, 77391</span>
      </li>
    </ul>
    <footer class="back__footer">
      <div class="person">
        <p class="person__name">GAVIN ALCOTT</p>
        <p class="person__role">Manager</p>
      </div>
    </footer>
  </div>
</section>

</body>
</html>
```